Memoir author looking for book cover design

Title:
"Rain, Rust and Return"

Subtitle:
"A Season Spent Chasing Our Father Across the Coastline"

My book is about the 18-month-long search and grieving process after my husband went missing from a hiking accident.
See "notesbeyondthequietharbor.example" for background

(An "ampersand" may look best, but I'm unable to enter it in this format)

Reason: Having difficulty finishing up, in part due to time difference. Don't want designers to have to work in the middle of the night!

```html
<!DOCTYPE html>
<html lang="en">
<head>
<meta charset="utf-8">
<title>Rain, Rust and Return — Book Cover</title>
<link rel="stylesheet" href="https://fonts.googleapis.com/css2?family=Anton&family=Great+Vibes&family=Oswald:wght@600;700&family=Open+Sans:ital,wght@0,600;1,700&display=swap">
<style>
  :root {
    --purple: #4b2a86;
    --pink: #e84a6f;
    --ink: #2e2e2e;
    --paper: #ffffff;
    --sky-top: #8f969c;
    --sky-mid: #c9ced3;
    --ridge: #7f8fa0;
    --valley: #3f5161;
  }
  * { margin: 0; padding: 0; box-sizing: border-box; }
  html, body { width: 795px; height: 1200px; overflow: hidden; background: var(--paper); }
  .cover { position: relative; width: 795px; height: 1200px; overflow: hidden; background: var(--paper); }
  .scenery {
    position: absolute; left: 0; top: 0; width: 795px; height: 975px;
    background: linear-gradient(180deg, var(--sky-top) 0%, var(--sky-mid) 28%, #dfe2e5 42%, var(--ridge) 62%, var(--valley) 100%);
  }
  .title { position: absolute; left: 0; top: 0; width: 795px; height: 330px; }
  .title .script { font-family: "Great Vibes", cursive; fill: var(--pink); }
  .title .block { font-family: "Oswald", sans-serif; font-weight: 700; fill: var(--purple); }
  .emblem { position: absolute; left: 0; top: 0; width: 795px; height: 975px; }
  .emblem-glyph { font-family: "Anton", sans-serif; }
  .band {
    position: absolute; left: 0; top: 975px; width: 795px; height: 225px;
    background: var(--paper); text-align: center;
  }
  .subtitle {
    font-family: "Open Sans", sans-serif; font-style: italic; font-weight: 700;
    color: var(--purple); font-size: 29px; line-height: 38px; margin-top: 22px;
  }
  .divider {
    width: 218px; height: 0; margin: 33px auto 0;
    border-top: 3px dotted var(--pink);
  }
  .author {
    font-family: "Open Sans", sans-serif; font-weight: 600; color: var(--ink);
    font-size: 25px; letter-spacing: 1.5px; margin-top: 20px;
  }
</style>
</head>
<body>
<main class="cover">
  <div class="scenery" role="img" aria-label="Cloudy sky over forested mountain ridges with a helicopter flying at left"></div>

  <svg class="emblem" viewBox="0 0 795 975" role="img" aria-label="Large ampersand framing a photo of a hiker with a backpack standing on a rocky mountain summit">
    <defs>
      <linearGradient id="summit" x1="0" y1="0" x2="0" y2="1">
        <stop offset="0" stop-color="#3f6fa8"/>
        <stop offset="0.3" stop-color="#7ea3c6"/>
        <stop offset="0.45" stop-color="#7d8f74"/>
        <stop offset="0.75" stop-color="#5a7040"/>
        <stop offset="1" stop-color="#6e6a5e"/>
      </linearGradient>
    </defs>
    <text class="emblem-glyph" x="140" y="930" font-size="860" textLength="520" lengthAdjust="spacingAndGlyphs"
          fill="url(#summit)" stroke="#ffffff" stroke-width="12" paint-order="stroke" stroke-linejoin="round">&amp;</text>
  </svg>

  <svg class="title" viewBox="0 0 795 330" aria-labelledby="book-title">
    <title id="book-title">Rain, Rust and Return</title>
    <text class="script" x="118" y="270" font-size="300">R</text>
    <text class="block" x="272" y="145" font-size="92" textLength="120" lengthAdjust="spacingAndGlyphs">AIN,</text>
    <text class="block" x="272" y="236" font-size="92" textLength="112" lengthAdjust="spacingAndGlyphs">UST</text>
    <text class="script" x="392" y="262" font-size="240">&amp;</text>
    <text class="block" x="555" y="236" font-size="130">R</text>
    <text class="block" x="618" y="236" font-size="92" textLength="128" lengthAdjust="spacingAndGlyphs">ETURN</text>
  </svg>

  <section class="band">
    <p class="subtitle">A Season Spent Chasing Our Father<br>Across the Coastline</p>
    <div class="divider"></div>
    <p class="author">Dana Whitlock</p>
  </section>
</main>
</body>
</html>
```